Personal Business Card Design Project

I am looking for a business card to be able to hand to both Chinese and Australian businessman.
I am a self employed consultant and just need my name, phone number and email address on the card. No Business Name and No Website.
I want it to look like an exclusive prestigious card.
I would like the background to be be a glossy red and the writing to be gold. (This applies to both sides of the card).
It must have English on one side and Chinese (Mandarin) on the reverse.
Details you will require
Name : Derek Hollins
Phone : + 61 428 903 574
Email : derekhollins@mailvanto.com
Updates
Thank you everybody for your designs.
Industry/Entity Type
Business

```html
<!DOCTYPE html>
<html lang="en">
<head>
<meta charset="utf-8">
<title>Derek Hollins – Business Card</title>
<link rel="stylesheet" href="https://fonts.googleapis.com/css2?family=Italianno&family=Jost:wght@400&display=swap">
<style>
  :root {
    --page-bg: #ece8e2;
    --card-red: #b81a2b;
    --card-red-deep: #a0121f;
    --gold-light: #f6e27a;
    --gold-mid: #dcb43c;
    --gold-deep: #b8892a;
  }
  html, body {
    margin: 0;
    width: 1200px;
    height: 800px;
    overflow: hidden;
    background: var(--page-bg);
  }
  .canvas {
    position: relative;
    width: 1200px;
    height: 800px;
    display: flex;
    align-items: center;
    justify-content: center;
  }
  .business-card {
    position: relative;
    width: 960px;
    height: 585px;
    background: linear-gradient(160deg, var(--card-red) 0%, var(--card-red) 60%, var(--card-red-deep) 100%);
    box-shadow: 0 10px 30px rgba(0, 0, 0, 0.18);
    overflow: hidden;
  }
  .gold-text {
    background: linear-gradient(180deg, var(--gold-light) 0%, var(--gold-mid) 50%, var(--gold-deep) 100%);
    -webkit-background-clip: text;
    background-clip: text;
    color: transparent;
  }
  .holder-name {
    position: absolute;
    left: 0;
    right: 0;
    top: 170px;
    margin: 0;
    padding-left: 40px;
    text-align: center;
    font-family: "Italianno", cursive;
    font-weight: 400;
    font-size: 178px;
    line-height: 1.1;
    white-space: nowrap;
    letter-spacing: 1px;
  }
  .contact-line {
    position: absolute;
    left: 80px;
    bottom: 62px;
    margin: 0;
    font-family: "Jost", sans-serif;
    font-size: 31px;
    letter-spacing: 1px;
    white-space: nowrap;
  }
  .contact-line .separator {
    margin: 0 20px;
  }
</style>
</head>
<body>
  <main class="canvas">
    <section class="business-card">
      <h1 class="holder-name gold-text">Derek Hollins</h1>
      <p class="contact-line gold-text">
        <span class="phone">+ 61 428 903 574</span><span class="separator">•</span><span class="email">derekhollins@mailvanto.com</span>
      </p>
    </section>
  </main>
</body>
</html>
```